Relationship Seminar

I am an Author and Speaker and I need a flyer for a Christian relationship seminar targeting women aged between mid 20's to late 30's. It's an event for women only.

-I am looking for a fresh/ edgy look but still feminine
-Nothing too girly
-Maximum of 3 colours (Spring colours are good)
-I want the flyer to convey joy or happiness
-Use my photo which is attached as the predominant image (you can crop it to remove the background etc)

The Flyer Details are as follows:

Somewhere Along The Way - Brisbane Tour

Join Author & Speaker, Rosalind Kupferle, as she speaks about her new book entitled 'Somewhere Along The Way'.

Be inspired and encouraged to embrace the life that God has given you and make the most of it!

Date: Saturday 9th November 2013
Time: 2:00 pm - 5:00 pm
Location: Harwick Lodge Brisbane (Juniper Hall)
Pelham Crescent, Brisbane QLD 4000
Tickets: $60/pp (Includes High Tea)
Buy Tickets: www.rosalindkupferle.com or http://somewherealongtheway.ticketquarry.net

Email: info@rosalindkupferle.com

Include the cover of my new book.

www.rosalindkupferle.com (include my website at the bottom of the flyer)

Target Market(s)

Young professional women aged between their mid 20's to late 30's

Industry/Entity Type

Event

Requirements
Should not have
• -No girly or curly font

```html
<!DOCTYPE html>
<html lang="en">
<head>
<meta charset="utf-8">
<title>Somewhere Along The Way – Brisbane Tour</title>
<link rel="stylesheet" href="https://fonts.googleapis.com/css2?family=Lato:wght@400;700&family=Cousine:ital,wght@1,400;1,700&display=swap">
<style>
  :root {
    --paper: #ffffff;
    --flame: #f15a22;
    --spring: #7cc242;
    --lilac: #a77cc4;
    --brick: #c9bcb2;
    --brick-light: #ebe5df;
    --coat: #2a2a2a;
    --ring: #eaf5df;
  }
  * { margin: 0; padding: 0; box-sizing: border-box; }
  html, body { width: 848px; height: 1200px; overflow: hidden; background: var(--paper); }
  .flyer {
    position: relative;
    width: 848px;
    height: 1200px;
    background: var(--paper);
    font-family: "Lato", Arial, sans-serif;
    overflow: hidden;
  }
  .event-title {
    position: absolute;
    top: 40px; left: 0; width: 100%;
    text-align: center;
    font-size: 56px;
    font-weight: 400;
    color: var(--flame);
    letter-spacing: 1px;
  }
  .tour-name {
    position: absolute;
    top: 124px; right: 90px;
    font-size: 35px;
    color: var(--spring);
    letter-spacing: 1px;
  }
  .hero-photo {
    position: absolute;
    top: 170px; left: 0;
    width: 848px; height: 400px;
    background:
      radial-gradient(ellipse 150px 200px at 62% 55%, var(--coat) 0%, #3b3030 60%, transparent 61%),
      linear-gradient(90deg, var(--brick-light) 0%, var(--brick) 55%, var(--brick-light) 100%);
  }
  .ring-pattern {
    position: absolute;
    top: 700px; left: 0;
    width: 640px; height: 440px;
    background: radial-gradient(circle at 40% 45%, var(--ring) 0%, rgba(234,245,223,0.5) 45%, rgba(255,255,255,0) 70%);
  }
  .book-cover {
    position: absolute;
    top: 372px; left: 40px;
    width: 218px; height: 336px;
    background: linear-gradient(180deg, #ffffff 0%, #f2f2f0 70%, #cfe6b8 100%);
    box-shadow: 6px 6px 12px rgba(0,0,0,0.25);
    border-left: 10px solid #e2e2e2;
  }
  .intro {
    position: absolute;
    top: 596px; left: 284px;
    width: 480px;
    font-size: 22px;
    line-height: 29px;
    color: var(--flame);
  }
  .intro strong { font-weight: 700; }
  .event-details {
    position: absolute;
    top: 776px; right: 28px;
    text-align: right;
    font-family: "Cousine", "Courier New", monospace;
    font-style: italic;
    font-size: 19px;
    line-height: 27.5px;
    color: var(--spring);
  }
  .tagline {
    position: absolute;
    top: 1042px; left: 0; width: 100%;
    text-align: center;
    font-family: "Cousine", "Courier New", monospace;
    font-style: italic;
    font-weight: 700;
    font-size: 20px;
    line-height: 29px;
    color: var(--lilac);
  }
  .website {
    position: absolute;
    top: 1142px; left: 0; width: 100%;
    text-align: center;
    font-family: "Cousine", "Courier New", monospace;
    font-weight: 700;
    font-size: 26px;
    letter-spacing: 7px;
    color: var(--spring);
  }
</style>
</head>
<body>
<main class="flyer">
  <h1 class="event-title">Somewhere Along The Way</h1>
  <p class="tour-name">...Brisbane Tour</p>

  <div class="hero-photo" role="img" aria-label="Photograph of the author smiling in a dark jacket against a whitewashed brick wall, with orange floral swirl ornaments on both sides"></div>

  <div class="ring-pattern" role="img" aria-label="Faint pale green concentric circle pattern"></div>

  <div class="book-cover" role="img" aria-label="Cover of the book 'Somewhere Along The Way' showing a woman in a white dress between two men"></div>

  <p class="intro">
    <strong>Join Author &amp; Speaker<br>Rosalind Kupferle</strong>, as she speaks about<br>her new book entitled<br>'Somewhere Along The Way'.
  </p>

  <div class="event-details">
    <p>Date: Saturday 9th November 2013</p>
    <p>Time: 2:00 pm - 5:00 pm</p>
    <p>Location: Harwick Lodge Brisbane (Juniper Hall)</p>
    <p>Pelham Crescent, Brisbane QLD 4000</p>
    <p>Tickets: $60/pp (Includes High Tea)</p>
    <p>Buy Tickets: www.rosalindkupferle.com or</p>
    <p>http://somewherealongtheway.ticketquarry.net</p>
    <p>Email: info@rosalindkupferle.com</p>
  </div>

  <p class="tagline">Be inspired and encouraged to embrace the life that<br>God has given you and make the most of it!</p>

  <p class="website">www.rosalindkupferle.com</p>
</main>
</body>
</html>
```